Cosmetic injections clinic needs a fresh looking business card

We need a business card using the supplied logo and color scheme to attract future clients to our clinic. It should be modern and fresh, eye catching and not too busy. Simple and to the point is best. I would like two sided designs with the front indicating address and contact information, and the back in full color with white logo and descriptive information also provided.
Target Market(s)
Clients looking for non surgical beauty enhancements.
Contact Information for Business Card
MeloraSkin
14, 618 Birchmont Way
St. Albert, Alberta
K2P 7W3
Phone: 587-412-6630
Email: info@meloraskin.com
Requirements
Must have
- -Logo supplied with the name and address of the clinic
- -Back of card in full color with white logo with A small line of text indicating both of the following: Anti aging consultants and cosmetic injectables
- Located inside the Voyager Wellness Group

```html
<!DOCTYPE html>
<html lang="en">
<head>
<meta charset="utf-8">
<title>MeloraSkin Business Card</title>
<link href="https://fonts.googleapis.com/css2?family=Montserrat:wght@700;800&family=Quicksand:wght@400;500&display=swap" rel="stylesheet">
<style>
  :root {
    --stage: #2b2b2b;
    --cream: #efe4d8;
    --cream-light: #f7f0e8;
    --brand-purple: #6b47a0;
    --brand-pink: #e2449a;
    --band-pink: #ea5fa6;
    --band-grey: #e4e4e6;
    --band-violet: #7d6bb5;
    --ink: #111111;
    --back-green: #79ab98;
    --back-violet: #a08ab8;
    --back-pink: #e26a98;
    --white: #ffffff;
  }
  * { margin: 0; padding: 0; box-sizing: border-box; }
  html, body { width: 1200px; height: 1200px; overflow: hidden; }
  body { background: var(--stage); position: relative; }

  .card { position: absolute; left: 138px; width: 935px; height: 535px; overflow: hidden; }
  .card--front { top: 50px; background: radial-gradient(ellipse at 60% 30%, var(--cream-light), var(--cream)); }
  .card--back { top: 614px; background: linear-gradient(105deg, var(--back-green) 0%, var(--back-violet) 45%, var(--back-pink) 100%); }

  .front-bands { position: absolute; inset: 0; width: 100%; height: 100%; }

  .brand-mark { position: absolute; border-radius: 50%; }
  .card--front .brand-mark { left: 134px; top: 70px; width: 208px; height: 208px; background: var(--brand-purple); }
  .card--back .brand-mark { left: 30px; top: 220px; width: 230px; height: 230px; background: var(--white); }

  .brand-name { position: absolute; font-family: "Montserrat", sans-serif; font-weight: 800; white-space: nowrap; }
  .card--front .brand-name { left: 390px; top: 165px; font-size: 64px; color: var(--brand-purple); }
  .card--back .brand-name { left: 300px; top: 310px; font-family: "Quicksand", sans-serif; font-weight: 500; font-size: 96px; color: var(--white); }

  .address { position: absolute; left: 12px; top: 344px; font-family: "Montserrat", sans-serif; font-weight: 800; color: var(--ink); }
  .address__label { font-size: 19px; line-height: 26px; font-weight: 700; }
  .address__line { font-size: 24px; line-height: 32px; }

  .contact { position: absolute; right: 9px; top: 440px; text-align: right; font-family: "Montserrat", sans-serif; font-weight: 700; font-size: 19px; line-height: 28px; color: var(--ink); }

  .tagline { position: absolute; font-family: "Quicksand", sans-serif; font-weight: 400; font-size: 41px; color: var(--white); white-space: nowrap; }
  .tagline--first { left: 352px; top: 86px; }
  .tagline--second { right: 29px; top: 140px; }
</style>
</head>
<body>
  <section class="card card--front">
    <svg class="front-bands" viewBox="0 0 935 535" preserveAspectRatio="none" aria-hidden="true">
      <defs>
        <linearGradient id="pinkBand" x1="0" y1="0" x2="1" y2="0">
          <stop offset="0" stop-color="var(--band-pink)"/>
          <stop offset="1" stop-color="var(--band-pink)" stop-opacity="0"/>
        </linearGradient>
        <linearGradient id="violetBand" x1="1" y1="0" x2="0" y2="0">
          <stop offset="0" stop-color="var(--band-violet)"/>
          <stop offset="1" stop-color="var(--band-violet)" stop-opacity="0"/>
        </linearGradient>
      </defs>
      <polygon points="0,316 700,390 0,535" fill="url(#pinkBand)"/>
      <polygon points="935,314 935,535 420,535" fill="url(#violetBand)" opacity="0.9"/>
      <polygon points="0,535 640,395 420,535" fill="var(--band-grey)" opacity="0.85"/>
    </svg>
    <div class="brand-mark" aria-hidden="true"></div>
    <div class="brand-name">MeloraSkin</div>
    <div class="address">
      <div class="address__label">Address :</div>
      <div class="address__line">MeloraSkin</div>
      <div class="address__line">14, 618 Birchmont Way</div>
      <div class="address__line">St. Albert, Alberta</div>
      <div class="address__line">K2P 7W3</div>
    </div>
    <div class="contact">
      <div>Phone: 587-412-6630</div>
      <div>Email: info@meloraskin.com</div>
    </div>
  </section>

  <section class="card card--back">
    <div class="tagline tagline--first">Anti aging consultants</div>
    <div class="tagline tagline--second">cosmetic injectables</div>
    <div class="brand-mark" aria-hidden="true"></div>
    <div class="brand-name">MeloraSkin</div>
  </section>
</body>
</html>
```